Tree company needs modern website design

We need a website design for a tree company, here are some websites they like:

http://korvalenboats.com/company/ - we like the big image filling most of the page. Also the top half of the page looks good with the logo along top and good task bar also (we don’t like the spiel on left hand side covering up the picture + too many words!) If we could have our logo at lop like this along with our slogan which is 'Great Looking Trees that Grow Well'

http://www.fernhollowplants.co.nz/ - we like the bottom half of this with the clean lines and welcome to part down bottom rather than the spiel to the left as on above site. Also like the moving leaves, any chance we could have birds such as a fantail, Tui and Bellbirds flying across the page and also some birdsong playing?

This is their existing website, that needs an updated design: http://tallmeadowgroves.co.nz/

Industry/Entity Type

It Company

Font styles to use
Serif
Sans Serif

Requirements
Must have
• "Website by Pixel Harbour Studio" located in bottom right hand side
Use images provided as background or banner images
Should not have
• Social Media icons

```html
<!DOCTYPE html>
<html lang="en">
<head>
<meta charset="utf-8">
<title>Tall Meadow Groves – Great Looking Trees That Grow Well</title>
<link rel="stylesheet" href="https://fonts.googleapis.com/css2?family=PT+Sans:wght@400;700&family=Questrial&display=swap">
<style>
:root{
  --yellow:#f3e61b;
  --white:#ffffff;
  --text-light:#e4e6d6;
  --text-muted:#c9ccbb;
  --panel:rgba(20,26,8,0.55);
  --card:rgba(18,22,6,0.55);
  --header:rgba(25,28,15,0.6);
  --rule:rgba(255,255,255,0.12);
  --btn-green:#4f6a1c;
}
*{margin:0;padding:0;box-sizing:border-box}
html,body{width:1200px;height:956px;overflow:hidden}
body{position:relative;font-family:"PT Sans",Arial,sans-serif;color:var(--white);background:#2d3a0c}
.backdrop{position:absolute;inset:0;
  background:
   radial-gradient(ellipse 260px 200px at 560px 150px,rgba(255,250,200,.95),rgba(240,230,120,.4) 55%,transparent 100%),
   linear-gradient(180deg,#55663a 0%,#6f7f3a 30%,#5e7a1c 55%,#8aa525 75%,#4f6a10 100%)}
.backdrop::before{content:"";position:absolute;inset:0;
  background:linear-gradient(90deg,rgba(20,25,10,.55) 0%,transparent 22%,transparent 78%,rgba(20,25,10,.55) 100%)}
.abs{position:absolute}
.site-header{left:240px;top:0;width:720px;height:77px;background:var(--header)}
.brand{left:28px;top:24px;display:flex;align-items:center;gap:8px;font-weight:700;font-size:17px;color:var(--yellow);letter-spacing:.5px}
.brand .mark{width:22px;height:22px;border-radius:50%;background:var(--yellow)}
.phone{left:532px;top:16px;font-size:13px;color:var(--yellow);letter-spacing:1px}
.main-nav{right:12px;top:45px;display:flex;gap:18px;font-size:10px;text-transform:uppercase}
.main-nav a{color:var(--white);text-decoration:none;padding-bottom:8px}
.main-nav a.active{color:var(--yellow);border-bottom:2px solid var(--yellow)}
.hero-title{left:240px;width:720px;top:120px;text-align:center;font-family:"Questrial",sans-serif;font-size:33px;color:var(--yellow);text-shadow:0 0 1px #776f00,1px 1px 2px rgba(0,0,0,.4)}
.hero-text{left:240px;width:720px;top:163px;text-align:center;font-size:13px;line-height:15px;color:#1e2210}
.hero-btn{left:553px;top:209px;width:100px;height:20px;background:var(--btn-green);border-radius:3px;color:var(--yellow);font-size:12px;text-align:center;line-height:20px}
.content{left:240px;top:270px;width:720px;height:648px;background:var(--panel)}
.slogan{left:0;width:720px;top:8px;text-align:center;font-family:"Questrial",sans-serif;font-size:21px;color:var(--yellow);text-transform:uppercase}
.slogan-rule{left:0;top:45px;width:720px;height:1px;background:var(--rule)}
.card{top:57px;width:203px;height:290px;background:var(--card);border:1px solid rgba(255,255,255,.06)}
.card h2{position:absolute;top:9px;width:100%;text-align:center;font-size:16px;font-weight:700;color:var(--yellow)}
.card .photo{position:absolute;left:21px;top:48px;width:160px;height:160px;border-radius:50%;border:2px solid #222;box-shadow:0 2px 6px rgba(0,0,0,.6)}
.card p{position:absolute;left:6px;right:6px;top:216px;text-align:center;font-family:Arial,sans-serif;font-size:8.6px;line-height:10.5px;letter-spacing:-.1px;color:var(--text-light)}
.card .more{position:absolute;top:262px;width:100%;text-align:center;font-size:12px;color:var(--white)}
.more::after{content:" ›";font-weight:700}
.section-rule{left:0;width:720px;height:1px;background:var(--rule)}
.welcome{left:20px;top:368px;width:380px}
.welcome h3,.newsletter h3{font-size:16px;font-weight:700;color:var(--yellow)}
.welcome p{font-family:Arial,sans-serif;font-size:8.5px;line-height:13px;color:var(--text-light);margin-top:3px}
.welcome p+p{margin-top:12px}
.welcome b{color:var(--white)}
.newsletter{left:429px;top:368px;width:270px}
.newsletter small{display:block;font-family:Arial,sans-serif;font-size:8px;font-weight:700;margin-top:2px}
.newsletter .field{margin-top:5px;height:28px;border:1px solid #777;border-radius:2px;background:rgba(0,0,0,.25)}
.newsletter .cta{margin:6px 0 0 auto;width:147px;height:22px;background:var(--yellow);border-radius:2px;color:#343a08;font-size:12px;font-weight:700;text-align:center;line-height:22px}
.foot-col{top:505px;font-size:8.5px;font-family:Arial,sans-serif;color:var(--text-muted);line-height:12.5px}
.foot-col h4{font-family:"PT Sans",sans-serif;font-size:13px;color:var(--white);margin-bottom:6px;line-height:16px}
.vrule{top:507px;width:1px;height:100px;background:var(--rule)}
.blog b{color:var(--white);display:block}
.copyright,.credit{top:666px;font-family:Arial,sans-serif;font-size:7.5px;color:#b8bca8}
.copyright{left:22px}
.credit{right:20px}
</style>
</head>
<body>
<div class="backdrop" role="img" aria-label="Blurred sunlit forest with tall trees and green grass"></div>

<header class="abs site-header">
  <div class="abs brand"><span class="mark"></span>TALL MEADOW GROVES</div>
  <div class="abs phone">0508 447 902</div>
  <nav class="abs main-nav">
    <a class="active">Home</a><a>About Us</a><a>Tree Gallery</a><a>Projects</a><a>Catalogue</a><a>Contact</a>
  </nav>
</header>

<h1 class="abs hero-title">Carpinus betulus - Hornbeam</h1>
<p class="abs hero-text">Hornbeam. A hardy deciduous smaller tree or<br>shrub with lush green spring/summer foliage, excellent for hedging.</p>
<div class="abs hero-btn">read more ›</div>

<main class="abs content">
  <div class="abs slogan">Great Looking Trees That Grow Well</div>
  <div class="abs slogan-rule"></div>

  <section class="abs card" style="left:21px">
    <h2>ABOUT US</h2>
    <div class="photo" role="img" aria-label="Gravel road lined with young trees under blue sky" style="background:linear-gradient(180deg,#3f76c8 0%,#cfe0f2 45%,#6c7a40 70%,#9c9a8a 100%)"></div>
    <p>Sed ut perspiciatis unde omnis iste natus error sit voluptatem accusan tium doloremque lau-dantium, totam rem aperiam, eaque ipsa quae ab illo tecto beatae vitae dicta..</p>
    <div class="more">read more</div>
  </section>
  <section class="abs card" style="left:258px">
    <h2>PROJECTS</h2>
    <div class="photo" role="img" aria-label="House with garden below rugged mountains" style="background:linear-gradient(180deg,#3d7fd6 0%,#8a8a86 35%,#6f6a5e 55%,#5f7a3a 80%,#4b6a24 100%)"></div>
    <p>Sed ut perspiciatis unde omnis iste natus error sit voluptatem accusan tium doloremque lau-dantium, totam rem aperiam, eaque ipsa quae ab illo tecto beatae vitae dicta..</p>
    <div class="more">read more</div>
  </section>
  <section class="abs card" style="left:496px">
    <h2>CATALOGUE</h2>
    <div class="photo" role="img" aria-label="Stone apartment building with planted trees" style="background:linear-gradient(90deg,#5a5550 0%,#7a7068 40%,#8a7a60 60%,#b9c8d8 100%)"></div>
    <p>Sed ut perspiciatis unde omnis iste natus error sit voluptatem accusan tium doloremque lau-dantium, totam rem aperiam, eaque ipsa quae ab illo tecto beatae vitae dicta..</p>
    <div class="more">read more</div>
  </section>

  <div class="abs section-rule" style="top:360px"></div>

  <section class="abs welcome">
    <h3>Welcome to TALL MEADOW GROVES ltd.</h3>
    <p><b>Curabitur non sem magna.</b> Proin luctus condimentum dapibus. Nullam lacus erat, tris tique sed tempor in, ornare ac augue. Mauris tincidunt, nisi eget vulputate rhoncus, nisl enim interdum risus, a commodo purus enim in eros.</p>
    <p>Vestibulum sit <b>amet leo quis neque postincidunt nulla</b>. Nuere mollis tincidunt nulla. Vivamus nvitae Nam consectetur purus tesquesellus variustempus sapien...</p>
  </section>

  <section class="abs newsletter">
    <h3>News letter</h3>
    <small>Subscribe to Our News letter, stay updated.</small>
    <div class="field"></div>
    <div class="cta">Get Started Today ▸</div>
  </section>

  <div class="abs section-rule" style="top:487px"></div>

  <div class="abs foot-col" style="left:21px"><h4>Quick Links</h4>Home<br>The Club<br>Services<br>Staff<br>Classes<br>Class Schedule<br>Join</div>
  <div class="abs vrule" style="left:104px"></div>
  <div class="abs foot-col" style="left:131px;top:527px">News<br>Blog<br>Hours<br>Gift Cards<br>Contact Us<br>Careers</div>
  <div class="abs vrule" style="left:199px"></div>
  <div class="abs foot-col" style="left:224px"><h4>Carrers</h4>Phone Operator<br>Tutor<br>Sweeper</div>
  <div class="abs vrule" style="left:302px"></div>
  <div class="abs foot-col" style="left:330px"><h4>Connect</h4>Birdcall<br>Leafpage<br>Grovecast<br>Snapwood<br>Reelbark<br>Twigpost</div>
  <div class="abs vrule" style="left:394px"></div>
  <div class="abs foot-col blog" style="left:423px;width:277px"><h4>Latest Blog</h4><b>Post Heading Goes Here</b>accusamus et iusto odio dignissimos ducimus qui blanditiis praesentium volupta tum deleniti atque corrupti quos dolores et quas molestias excepturi sint occae cati cupid itate non provident, similique sunt in culpa qui officia deserunt mollitia animi, id est laborum..<br>read more »</div>

  <div class="abs section-rule" style="top:648px;background:rgba(255,255,255,.18)"></div>
  <div class="abs copyright">© Copyright  tallmeadowgroves.co.nz  All Rights Reserved.</div>
  <div class="abs credit">Website by Pixel Harbour Studio</div>
</main>
</body>
</html>
```